Tradeshow Display for Geothermal Installation Company
Green, Cost-effective energy
Tradeshow Display for Geothermal Installation Company - Home and Garden
Creative Brief
We are Brightmoor Powerworks, a company that revolutionizes how people think about green energy. Through geothermal technology, we help homeowners use green energy that's right beneath their feet to save thousands of dollars annually. We are going to be taking this tradeshow display to fairs and home and garden shows to market ourselves to potential buyers. Here's the display we're going to buy: http://www.plinvex.com/Tall-Arch-10ft-Pop-Up-Trade-Show-Display-Graphic-p/ta10g.htm Here's our logo: http://www.brightmoorpowerworks.com/wp-content/uploads/2012/02/logoforweb6atsize1.png Our website is not final, so don't use that as a guide. DO however, use the logo as a guide, and include it in the design. Here's some designs people have done with the same sign: http://www.plinvex.com/PhotoGallery.asp?ProductCode=TA10G We like the one with the lightbulb, the one with the rockers, and the "revitalized" water one. We dislike the "KRV Harbor", "Vendal Trust", and "Quorvane". It needs to have a very dignified, yet undeniably cool feel to the whole thing. Perhaps minimalist. We think Tindle products do a good job of exemplifying this. Sometimes simpler is better. We're excited to see what you come up with!
Home and Garden
Homeowners on the upper end of the income spectrum.
Design must include our logo prominently. Final design must be 159.812"W x 88.98"H, at 125 dpi or higher. For more information go to http://www.plinvex.com/Articles.asp?ID=141 We are buying the Tall Arch 10ft Pop up Tradeshow Display. You can find templates and specifications at the website above.

```html
<!DOCTYPE html>
<html lang="en">
<head>
<meta charset="utf-8">
<title>Brightmoor Powerworks – Tradeshow Display</title>
<link rel="stylesheet" href="https://fonts.googleapis.com/css2?family=Roboto+Condensed:ital,wght@0,700;1,400&display=swap">
<style>
  :root {
    --sky-light: #ffffff;
    --sky-mid: #e6f3fb;
    --sky-deep: #aed8f0;
    --leaf-pale: #e4f2c8;
    --leaf: #8cc63f;
    --leaf-deep: #5fa82a;
    --brand-blue: #2a6fb6;
    --brand-green: #69b32f;
    --ink: #3a3a3a;
    --bulb-glass: #eef3f6;
    --bulb-shade: #c9d3da;
  }
  * { margin: 0; padding: 0; box-sizing: border-box; }
  html, body { width: 1200px; height: 667px; overflow: hidden; }
  body { background: #ffffff; }
  .display {
    position: relative;
    width: 1200px;
    height: 667px;
    overflow: hidden;
    background: linear-gradient(90deg, var(--sky-light) 0%, var(--sky-light) 35%, var(--sky-mid) 65%, var(--sky-deep) 100%);
  }
  .swoosh {
    position: absolute;
    inset: 0;
    width: 1200px;
    height: 667px;
  }
  .brand {
    position: absolute;
    left: 320px;
    top: 150px;
    display: flex;
    align-items: center;
    gap: 36px;
  }
  .brand-dot {
    width: 190px;
    height: 190px;
    border-radius: 50%;
    background: var(--brand-green);
    flex: none;
  }
  .brand-name {
    font-family: "Roboto Condensed", sans-serif;
    font-weight: 700;
    font-size: 76px;
    line-height: 0.95;
    color: var(--brand-blue);
    letter-spacing: -0.5px;
  }
  .bulb {
    position: absolute;
    left: 1068px;
    top: 56px;
    width: 150px;
    height: 390px;
    border-radius: 75px 0 0 60px;
    background: radial-gradient(ellipse at 60% 35%, var(--bulb-glass) 0%, #dde6ec 55%, var(--bulb-shade) 100%);
  }
  .tagline {
    position: absolute;
    left: 684px;
    top: 528px;
    font-family: "Roboto Condensed", sans-serif;
    font-style: italic;
    font-weight: 400;
    font-size: 35px;
    color: var(--ink);
    white-space: nowrap;
  }
</style>
</head>
<body>
<main class="display">
  <svg class="swoosh" viewBox="0 0 1200 667" aria-hidden="true">
    <defs>
      <linearGradient id="leaf-wash" x1="0" y1="0" x2="1" y2="0">
        <stop offset="0" stop-color="var(--leaf-pale)"/>
        <stop offset="1" stop-color="#ffffff"/>
      </linearGradient>
      <linearGradient id="leaf-band" x1="0" y1="0" x2="1" y2="1">
        <stop offset="0" stop-color="var(--leaf-deep)"/>
        <stop offset="1" stop-color="var(--leaf)"/>
      </linearGradient>
    </defs>
    <path d="M0,0 L280,0 C90,150 70,470 420,667 L0,667 Z" fill="url(#leaf-wash)"/>
    <path d="M280,0 C90,150 70,470 420,667 L380,667 C40,470 70,150 262,0 Z" fill="url(#leaf-band)" opacity="0.85"/>
    <path d="M0,470 C140,560 380,640 800,667 L560,667 C330,650 140,600 0,520 Z" fill="url(#leaf-band)"/>
    <path d="M0,430 C180,560 470,630 820,660" fill="none" stroke="var(--leaf)" stroke-width="3"/>
    <path d="M0,560 C150,620 330,655 520,667" fill="none" stroke="#ffffff" stroke-width="4" opacity="0.8"/>
    <path d="M268,0 C110,140 90,420 330,610" fill="none" stroke="#ffffff" stroke-width="3" opacity="0.8"/>
  </svg>

  <div class="brand">
    <span class="brand-dot"></span>
    <h1 class="brand-name">Brightmoor<br>Powerworks</h1>
  </div>

  <div class="bulb" role="img" aria-label="Photograph of a glowing light bulb, cropped at the right edge"></div>

  <p class="tagline">Green, Cost-effective energy</p>
</main>
</body>
</html>
```